Frostbarrow Harbor's Hymn Event Flyer - Fundraiser for a Vell Assembly Candidate

Working on an event flyer for a fundraiser for a Meridianist candidate for Assembly in Tennessee. Hosting an event for him that's a Frostbarrow Harbor's Hymn theme, and I need a cool flyer that fits the theme with event details.
Host names will be added to the flyer on an ongoing basis, so will need someone who can quickly add names to flyer as hosts commit. Would like to agree to a fee for all work up front.
I'm attaching a mockup of a flyer that my friend did, before he had to back out because of work commitments, as well as a couple of pieces of Frostbarrow Harbor's Hymn art that I think are cool.
Meridianist

```html
<!DOCTYPE html>
<html lang="en">
<head>
<meta charset="utf-8">
<title>Frostbarrow CPC Meeting Eve – Reception for Elias Wrenford</title>
<link rel="stylesheet" href="https://fonts.googleapis.com/css2?family=Great+Vibes&family=Dancing+Script:wght@600&family=Carlito:wght@400;700&display=swap">
<style>
  :root {
    --night: #0b1016;
    --dusk: #26313d;
    --haze: #b9ae98;
    --mist: #e7dfcd;
    --ink-white: #ffffff;
    --ice-blue: #a9d6f2;
    --soft-white: #f2f2f2;
  }
  html, body {
    margin: 0;
    padding: 0;
    width: 1200px;
    height: 675px;
    overflow: hidden;
    background: var(--night);
  }
  .flyer {
    position: relative;
    width: 1200px;
    height: 675px;
    overflow: hidden;
    color: var(--ink-white);
  }
  .scene {
    position: absolute;
    inset: 0;
    background:
      radial-gradient(ellipse 45% 40% at 50% 42%, rgba(231,223,205,0.55), rgba(231,223,205,0) 70%),
      radial-gradient(ellipse 22% 18% at 82% 52%, rgba(231,223,205,0.5), rgba(231,223,205,0) 70%),
      radial-gradient(ellipse 20% 18% at 20% 52%, rgba(231,223,205,0.35), rgba(231,223,205,0) 70%),
      linear-gradient(180deg, #1a222c 0%, #4f5a63 28%, var(--haze) 50%, #5b5a55 64%, #262a2c 78%, var(--night) 100%);
  }
  .scene::after {
    content: "";
    position: absolute;
    inset: 0;
    background:
      linear-gradient(90deg, rgba(11,16,22,0.85) 0%, rgba(11,16,22,0) 12%, rgba(11,16,22,0) 88%, rgba(11,16,22,0.85) 100%),
      linear-gradient(180deg, rgba(11,16,22,0.7) 0%, rgba(11,16,22,0) 22%);
  }
  .title {
    position: absolute;
    font-family: "Great Vibes", cursive;
    color: var(--ink-white);
    line-height: 1;
    white-space: nowrap;
    text-shadow: 0 2px 6px rgba(0,0,0,0.45);
  }
  .title-a { left: 262px; top: 40px; font-size: 150px; }
  .title-main { left: 70px; top: 135px; font-size: 112px; }
  .title-party { left: 118px; top: 222px; font-size: 104px; color: var(--ice-blue); }
  .title-meeting { left: 326px; top: 222px; font-size: 104px; }
  .title-eve { left: 420px; top: 300px; font-size: 92px; }
  .details {
    position: absolute;
    left: 650px;
    width: 550px;
    text-align: center;
    font-family: "Dancing Script", cursive;
    font-weight: 600;
    font-size: 29px;
    line-height: 38px;
    color: var(--ink-white);
    text-shadow: 0 1px 4px rgba(0,0,0,0.5);
  }
  .details-when { top: 198px; }
  .details-where { top: 308px; }
  .details sup { font-size: 0.55em; }
  .giving {
    position: absolute;
    left: 130px;
    width: 500px;
    text-align: center;
    font-family: "Carlito", sans-serif;
    color: var(--soft-white);
    text-shadow: 0 1px 3px rgba(0,0,0,0.6);
  }
  .giving-levels { top: 428px; font-size: 21px; line-height: 37px; }
  .giving-rsvp { top: 524px; font-size: 20px; line-height: 30px; }
  .rsvp-or {
    position: absolute;
    left: 606px;
    top: 538px;
    font-family: "Dancing Script", cursive;
    font-size: 24px;
    color: var(--soft-white);
  }
  .disclaimer {
    position: absolute;
    left: 753px;
    top: 502px;
    width: 356px;
    height: 27px;
    border: 1px solid var(--soft-white);
    display: flex;
    align-items: center;
    justify-content: center;
    font-family: "Carlito", sans-serif;
    font-variant: small-caps;
    font-size: 17px;
    letter-spacing: 1.2px;
    color: var(--soft-white);
  }
  .campaign-name {
    position: absolute;
    left: 832px;
    top: 556px;
    width: 200px;
    display: flex;
    align-items: center;
    justify-content: center;
    gap: 8px;
    font-family: "Carlito", sans-serif;
    font-weight: 700;
    font-size: 19px;
    color: var(--ink-white);
  }
  .campaign-mark {
    width: 10px;
    height: 10px;
    background: var(--ink-white);
  }
</style>
</head>
<body>
  <main class="flyer">
    <div class="scene" role="img" aria-label="Night forest clearing under starlit tree canopy, misty meadow with glowing hazy sky"></div>

    <div class="title title-a">A</div>
    <div class="title title-main">Frostbarrow's</div>
    <div class="title title-party">CPC</div>
    <div class="title title-meeting">Meeting</div>
    <div class="title title-eve">Eve</div>

    <div class="details details-when">
      Reception for Elias Wrenford<br>
      Wednesday, August 23<sup>rd</sup> 6<sup>00</sup>-9<sup>00</sup>pm
    </div>
    <div class="details details-where">
      Home of Conrad Ashby<br>
      417B Larkspur Ave, Nashville, TN 37209
    </div>

    <div class="giving giving-levels">
      Suggested Contribution:<br>
      $20.18 Friend | $100 Supporter | $250 Host
    </div>
    <div class="giving giving-rsvp">
      RSVP at www.EliasWrenford.com/Frostbarrow<br>
      RSVP by Email at RSVP@EliasWrenford.com
    </div>
    <div class="rsvp-or">or</div>

    <div class="disclaimer">Paid for by Wrenford for Vell Assembly</div>
    <div class="campaign-name"><span class="campaign-mark"></span>Elias Wrenford</div>
  </main>
</body>
</html>
```